Electrician Company Website Design

I am looking to get a website designed only. I do not need it converted ot html. I simply need the design in a psd format. I have my own team for the conversion. The website is for an electrician company called Bramblecourt electric. I have created a txt document with the project parameters and specifics. I have also uploaded their logo in all avaible formats. It's a zip file.

Number of Pages Required

1 page

```html
<!DOCTYPE html>
<html lang="en">
<head>
<meta charset="utf-8">
<title>Bramblecourt Electric</title>
<link rel="stylesheet" href="https://fonts.googleapis.com/css2?family=Oswald:wght@400;500;600;700&family=Roboto:wght@400;500&display=swap">
<style>
:root{
  --navy:#0b1f4d;
  --blue:#1450a3;
  --blue-deep:#0a3a86;
  --blue-bright:#2a6fd0;
  --red:#a31d24;
  --red-bright:#c8242c;
  --red-dark:#3a0608;
  --ink:#1c1c1c;
  --grey:#555;
  --pill:#f2f2f2;
  --white:#fff;
}
*{margin:0;padding:0;box-sizing:border-box}
html,body{width:1200px;height:4286px;overflow:hidden;background:var(--white)}
body{font-family:"Roboto",Arial,sans-serif;color:var(--ink)}
a{text-decoration:none}
.page{position:relative;width:1200px;height:4286px;overflow:hidden;background:var(--white)}
.abs{position:absolute}
.heading{font-family:"Oswald",Arial,sans-serif;font-weight:600;text-transform:uppercase;letter-spacing:.5px}
.bolt{position:absolute;left:50%;transform:translateX(-50%);width:32px;height:52px}
.btn{position:absolute;display:flex;align-items:center;justify-content:center;font-family:"Oswald",Arial,sans-serif;font-weight:600;color:var(--white);text-transform:uppercase;border-radius:22px;border:2px solid var(--white)}
.btn--red{background:var(--red);box-shadow:0 0 0 2px var(--red)}
.btn--blue{background:var(--blue);box-shadow:0 0 0 2px var(--blue)}

/* top bar & nav */
.topbar{top:0;left:0;width:1200px;height:50px;background:linear-gradient(90deg,var(--navy),var(--blue))}
.topbar__phone{right:200px;top:9px;display:flex;align-items:center;gap:10px;color:var(--white);font-weight:500;font-size:19px}
.icon-circle{width:32px;height:32px;border-radius:50%;background:var(--red-bright);display:flex;align-items:center;justify-content:center;flex:none}
.nav{top:50px;left:0;width:1200px;height:60px;background:var(--white);border-bottom:1px solid #ddd}
.nav a{position:absolute;top:21px;font-family:"Oswald",Arial,sans-serif;font-size:13px;color:var(--ink);text-transform:uppercase}
.nav a.is-active{color:var(--red-bright)}
.brand{left:492px;top:-36px;width:216px;height:216px;border-radius:50%;background:var(--white);border:6px solid var(--blue);display:flex;flex-direction:column;align-items:center;justify-content:center;padding-top:40px;font-family:"Oswald",Arial,sans-serif;font-weight:600;color:var(--navy);font-size:21px;line-height:1.15;text-align:center;z-index:5}

/* hero */
.hero{top:110px;left:0;width:1200px;height:790px;background:
  radial-gradient(circle at 77% 22%,#e6f0ff 0,#8fb3ea 5%,rgba(62,111,184,.7) 14%,rgba(20,42,85,0) 34%),
  radial-gradient(ellipse at 84% 62%,#4a4036 0,rgba(40,36,40,.85) 18%,rgba(20,30,60,0) 36%),
  radial-gradient(ellipse at 12% 80%,rgba(214,150,70,.55) 0,rgba(120,90,90,.3) 20%,rgba(20,30,60,0) 45%),
  radial-gradient(ellipse at 35% 95%,rgba(110,140,200,.5) 0,rgba(20,30,60,0) 40%),
  linear-gradient(180deg,#0a1430 0,#14264f 55%,#2a3a5e 100%)}
.hero__title{left:150px;top:288px;color:var(--white);font-size:52px;line-height:66px}
.hero__btn{left:153px;top:454px;width:197px;height:50px;font-size:22px}

/* blue band */
.band{top:990px;left:0;width:1200px;height:1120px;background:
  radial-gradient(ellipse 70% 14% at 50% 26%,rgba(150,190,255,.35),rgba(20,80,163,0)),
  radial-gradient(ellipse at 50% 30%,var(--blue-bright),var(--blue-deep) 70%)}

/* about */
.about{left:-38px;top:657px;width:1276px;height:541px;border-radius:50%;background:var(--white)}
.about__title{top:800px;left:0;width:1200px;text-align:center;font-size:44px}
.about__text{top:885px;left:211px;width:778px;text-align:center;font-size:12.5px;line-height:20.8px;color:#333}
.about__btn{left:536px;top:1052px;width:126px;height:38px;font-size:15px}

/* services */
.services__title{top:1312px;left:0;width:1200px;text-align:center;font-size:44px;color:var(--white)}
.service{width:276px;height:276px;border-radius:50%;border:6px solid var(--red);box-shadow:0 0 0 4px var(--white) inset;display:flex;align-items:flex-end;justify-content:center;padding-bottom:66px;font-family:"Oswald",Arial,sans-serif;font-weight:500;font-size:18px;color:var(--white);text-shadow:0 1px 3px rgba(0,0,0,.6);top:1421px}
.service--commercial{left:152px;background:radial-gradient(circle at 35% 35%,#d8dde2 0,#8a9aaa 30%,transparent 55%),radial-gradient(circle at 70% 60%,#b8b03a 0,#6c7250 25%,transparent 50%),radial-gradient(circle,#4e5e72,#243246)}
.service--residential{left:463px;background:radial-gradient(circle at 60% 30%,#e4e0d8 0,#a9a298 30%,transparent 55%),radial-gradient(circle at 35% 65%,#8a6a52 0,transparent 45%),radial-gradient(circle,#5e5a56,#2c2b30)}
.service--industrial{left:771px;background:radial-gradient(circle at 55% 40%,#c9b4a0 0,#6c7ea0 30%,transparent 55%),radial-gradient(circle at 30% 70%,#2c4a7c 0,transparent 45%),radial-gradient(circle,#33476e,#16223e)}
.services__btn{left:534px;top:1747px;width:130px;height:38px;font-size:15px}

/* service areas */
.areas{left:-400px;top:1864px;width:2000px;height:1830px;border-radius:50%;background:var(--white)}
.areas__title{top:2032px;left:0;width:1200px;text-align:center;font-size:40px}
.areas__intro{left:150px;top:2170px;width:360px;font-size:12.5px;line-height:20px;color:#333}
.areas__list{left:150px;top:2227px;list-style:none;font-family:"Oswald",Arial,sans-serif;font-size:17px}
.areas__list li{display:flex;align-items:center;gap:10px;height:36px}
.areas__list li.is-current{color:var(--blue);font-weight:500}
.areas__map{left:576px;top:2147px;width:244px;height:324px;border-radius:4px;background:
  radial-gradient(ellipse 35% 18% at 45% 63%,#1a5ab8 0,rgba(26,90,184,.6) 50%,rgba(26,90,184,0) 100%),
  linear-gradient(160deg,#d6d6d6,#b3b3b3)}
.areas__label{left:850px;top:2338px;font-family:"Roboto",Arial,sans-serif;font-weight:500;font-size:38px;line-height:50px;color:#444}
.areas__btn{left:153px;top:2426px;width:127px;height:38px;font-size:14px}

/* contact */
.contact{top:2584px;left:0;width:1200px;height:624px;background:
  radial-gradient(ellipse 12% 30% at 34% 48%,rgba(255,170,60,.55),rgba(200,30,30,0)),
  radial-gradient(ellipse at 30% 75%,#b0141b,var(--red-dark) 70%,#1a0203)}
.contact__title{left:150px;top:2688px;font-size:40px;color:var(--white)}
.field{position:absolute;left:150px;width:394px;height:40px;border:1.5px solid var(--white);color:var(--white);font-size:12.5px;padding:11px 13px}
.radios{left:150px;top:2990px;display:flex;gap:40px;color:var(--white);font-size:12.5px}
.radios span{display:flex;align-items:center;gap:7px}
.radios i{width:15px;height:15px;border-radius:50%;border:1.5px solid var(--white)}
.contact__btn{left:151px;top:3118px;width:100px;height:38px;font-size:14px}

/* faq */
.faq__title{top:3352px;left:0;width:1200px;text-align:center;font-size:40px}
.faq__item{left:271px;width:656px;height:50px;border-radius:25px;background:var(--pill);display:flex;align-items:center;justify-content:space-between;padding:0 30px;font-size:13.5px;color:#333}
.faq__item b{color:var(--red-bright);font-size:18px}
.faq__btn{left:541px;top:3811px;width:118px;height:38px;font-size:14px}

/* footer */
.footer__bg{top:3700px;left:0;width:1200px;height:586px}
.footer__brand{left:150px;top:4088px;display:flex;align-items:center;gap:12px;font-family:"Oswald",Arial,sans-serif;font-weight:600;font-size:22px;color:var(--white)}
.footer__brand i{width:22px;height:22px;border-radius:50%;background:var(--red-bright)}
.footer__head{top:4025px;font-size:21px;color:var(--white)}
.footer__row{left:483px;display:flex;align-items:center;gap:14px;color:var(--white);font-size:12.5px;line-height:17px}
.footer__link{font-size:12.5px;color:var(--white)}
.social{left:1012px;width:36px;height:36px;border-radius:50%;border:2px solid var(--white)}
.copyright{top:4251px;left:0;width:1200px;text-align:center;font-family:"Oswald",Arial,sans-serif;font-size:11px;color:var(--white);word-spacing:2px}
.copyright span{margin:0 10px}
</style>
</head>
<body>
<div class="page">

  <div class="abs hero" role="img" aria-label="Photo of an electrician in a hard hat joining two sparking cables above a city at night"></div>

  <div class="abs band" role="img" aria-label="Blue abstract background with light streaks"></div>

  <div class="abs topbar"></div>
  <div class="abs topbar__phone">
    <span class="icon-circle"><svg width="16" height="16" viewBox="0 0 24 24"><path fill="#fff" d="M6.6 10.8a15 15 0 0 0 6.6 6.6l2.2-2.2c.3-.3.7-.4 1-.2 1.1.4 2.3.6 3.6.6.6 0 1 .4 1 1V20c0 .6-.4 1-1 1A17 17 0 0 1 3 4c0-.6.4-1 1-1h3.5c.6 0 1 .4 1 1 0 1.3.2 2.5.6 3.6.1.3 0 .7-.2 1z"/></svg></span>
    555 014 2290
  </div>

  <nav class="abs nav">
    <a href="#" class="is-active" style="left:150px">Home</a>
    <a href="#" style="left:213px">Company</a>
    <a href="#" style="left:298px">Service Area</a>
    <a href="#" style="left:785px">Services</a>
    <a href="#" style="left:867px">Gallery</a>
    <a href="#" style="left:945px">Contact</a>
    <a href="#" style="left:1027px">FAQ</a>
  </nav>
  <div class="abs brand">BRAMBLECOURT<br>ELECTRIC</div>

  <h1 class="abs heading hero__title">Your Trusted<br>Electric Partner</h1>
  <a class="btn btn--red hero__btn" href="#">Get in Touch</a>

  <!-- about -->
  <div class="abs about"></div>
  <svg class="bolt" style="top:730px" viewBox="0 0 32 52"><path fill="#1c1c1c" d="M20 0 4 30h11l-3 22L28 20H17z"/></svg>
  <h2 class="abs heading about__title">About Us</h2>
  <p class="abs about__text">Lorem ipsum dolor sit amet, consectetur adipiscing elit, sed do eiusmod tempor incididunt ut labore et dolore magna aliqua. Ut enim ad minim veniam, quis nostrud exercitation ullamco laboris nisi ut aliquip ex ea commodo consequat. Duis aute irure dolor in reprehenderit in voluptate velit esse cillum dolore eu fugiat nulla pariatur. Excepteur sint occaecat cupidatat non proident, sunt in culpa qui officia deserunt mollit anim id est laborum.Sed ut perspiciatis unde omnis iste natus error sit voluptatem accusantium doloremque laudantium, totam rem aperiam, eaque ipsa quae ab illo inventore veritatis et quasi architecto beatae vitae dicta sunt explicabo. Nemo enim ipsam voluptatem quia voluptas sit aspernatur aut odit aut fugit, sed quia consequuntur magni dolores eos qui ratione voluptatem sequi nesciunt.</p>
  <a class="btn btn--blue about__btn" href="#">Read More</a>

  <!-- services -->
  <svg class="bolt" style="top:1246px" viewBox="0 0 32 52"><path fill="#fff" d="M20 0 4 30h11l-3 22L28 20H17z"/></svg>
  <h2 class="abs heading services__title">Our Services</h2>
  <div class="abs service service--commercial" role="img" aria-label="Photo of commercial electricians reviewing plans">Commercial Electrician</div>
  <div class="abs service service--residential" role="img" aria-label="Photo of a residential electrician on a ladder">Residential Electrician</div>
  <div class="abs service service--industrial" role="img" aria-label="Photo of an industrial plant interior">Industrial Electrician</div>
  <a class="btn btn--red services__btn" href="#">Learn More</a>

  <!-- service areas -->
  <div class="abs areas"></div>
  <svg class="bolt" style="top:1966px" viewBox="0 0 32 52"><path fill="#1c1c1c" d="M20 0 4 30h11l-3 22L28 20H17z"/></svg>
  <h2 class="abs heading areas__title">Service Areas</h2>
  <p class="abs areas__intro">Lorem ipsum dolor sit amet, consectetur adipiscing elit, sed do eiusmod tempor incididunt magna aliqua.</p>
  <ul class="abs areas__list">
    <li class="is-current"><svg width="16" height="20" viewBox="0 0 16 20"><path fill="#1c1c1c" d="M8 0a8 8 0 0 0-8 8c0 6 8 12 8 12s8-6 8-12a8 8 0 0 0-8-8zm0 11a3 3 0 1 1 0-6 3 3 0 0 1 0 6z"/></svg>Central Minnesota</li>
    <li><svg width="16" height="20" viewBox="0 0 16 20"><path fill="#a31d24" d="M8 0a8 8 0 0 0-8 8c0 6 8 12 8 12s8-6 8-12a8 8 0 0 0-8-8zm0 11a3 3 0 1 1 0-6 3 3 0 0 1 0 6z"/></svg>Duluth</li>
    <li><svg width="16" height="20" viewBox="0 0 16 20"><path fill="#a31d24" d="M8 0a8 8 0 0 0-8 8c0 6 8 12 8 12s8-6 8-12a8 8 0 0 0-8-8zm0 11a3 3 0 1 1 0-6 3 3 0 0 1 0 6z"/></svg>Fargo</li>
    <li><svg width="16" height="20" viewBox="0 0 16 20"><path fill="#a31d24" d="M8 0a8 8 0 0 0-8 8c0 6 8 12 8 12s8-6 8-12a8 8 0 0 0-8-8zm0 11a3 3 0 1 1 0-6 3 3 0 0 1 0 6z"/></svg>Southwest Minnesota</li>
    <li><svg width="16" height="20" viewBox="0 0 16 20"><path fill="#a31d24" d="M8 0a8 8 0 0 0-8 8c0 6 8 12 8 12s8-6 8-12a8 8 0 0 0-8-8zm0 11a3 3 0 1 1 0-6 3 3 0 0 1 0 6z"/></svg>Twin Cities</li>
  </ul>
  <a class="btn btn--blue areas__btn" href="#">Learn More</a>
  <div class="abs areas__map" role="img" aria-label="County map of Minnesota with the central service region highlighted in blue and area pins"></div>
  <p class="abs areas__label">Central<br>Minnesota</p>

  <!-- contact -->
  <div class="abs contact"></div>
  <svg class="abs" style="top:2584px;left:0" width="1200" height="624" viewBox="0 0 1200 624" role="img" aria-label="Photo of a technician in a blue hard hat working on a laptop beside an electrical panel">
    <defs>
      <linearGradient id="techTone" x1="0" y1="0" x2="1" y2="1"><stop offset="0" stop-color="#b8cde6"/><stop offset=".35" stop-color="#5d86c4"/><stop offset=".7" stop-color="#234c96"/><stop offset="1" stop-color="#182a4e"/></linearGradient>
      <radialGradient id="techGlow" cx=".75" cy=".3" r=".5"><stop offset="0" stop-color="#e8eef6" stop-opacity=".7"/><stop offset="1" stop-color="#e8eef6" stop-opacity="0"/></radialGradient>
    </defs>
    <path d="M740 0Q560 312 750 624H1200V0Z" fill="#fff"/>
    <path d="M752 0Q574 312 762 624H1200V0Z" fill="url(#techTone)"/>
    <path d="M752 0Q574 312 762 624H1200V0Z" fill="url(#techGlow)"/>
  </svg>
  <svg class="bolt" style="top:2620px;left:255px" viewBox="0 0 32 52"><path fill="#fff" d="M20 0 4 30h11l-3 22L28 20H17z"/></svg>
  <h2 class="abs heading contact__title">Contact Us</h2>
  <div class="field" style="top:2774px">Name</div>
  <div class="field" style="top:2827px">Email Address</div>
  <div class="field" style="top:2880px">Phone Number</div>
  <div class="field" style="top:2933px">Location</div>
  <div class="abs radios"><span><i></i>Commercial</span><span><i></i>Residential</span><span><i></i>Indusrial</span></div>
  <div class="field" style="top:3027px;height:68px">Message</div>
  <a class="btn btn--blue contact__btn" href="#">Submit</a>

  <!-- faq -->
  <svg class="bolt" style="top:3285px" viewBox="0 0 32 52"><path fill="#1c1c1c" d="M20 0 4 30h11l-3 22L28 20H17z"/></svg>
  <h2 class="abs heading faq__title">FAQ</h2>

  <!-- footer background -->
  <svg class="abs footer__bg" viewBox="0 0 1200 586" role="img" aria-label="Dark navy background with faint electric lines">
    <defs><linearGradient id="footTone" x1="0" y1="0" x2="0" y2="1"><stop offset="0" stop-color="#0a1a3a"/><stop offset="1" stop-color="#061026"/></linearGradient></defs>
    <path d="M0 11Q600 483 1200 11V586H0Z" fill="url(#footTone)"/>
    <path d="M0 11Q600 483 1200 11" fill="none" stroke="#a31d24" stroke-width="6"/>
  </svg>

  <div class="abs faq__item" style="top:3434px">1.Lorem ipsum dolor sit amet, consectetur adipiscing elit, sed do eiusmod tempor?<b>+</b></div>
  <div class="abs faq__item" style="top:3508px">2.Lorem ipsum dolor sit amet, consectetur adipiscing elit, sed do eiusmod tempor?<b>+</b></div>
  <div class="abs faq__item" style="top:3581px">3. Lorem ipsum dolor sit amet, consectetur adipiscing elit, sed do eiusmod tempor?<b>+</b></div>
  <div class="abs faq__item" style="top:3653px">4. Lorem ipsum dolor sit amet, consectetur adipiscing elit, sed do eiusmod tempor?<b>+</b></div>
  <div class="abs faq__item" style="top:3724px">5.Lorem ipsum dolor sit amet, consectetur adipiscing elit, sed do eiusmod tempor?<b>+</b></div>
  <a class="btn btn--blue faq__btn" href="#">View All</a>

  <!-- footer -->
  <div class="abs footer__brand"><i></i>BRAMBLECOURT ELECTRIC</div>

  <h3 class="abs heading footer__head" style="left:483px">Get in Touch</h3>
  <div class="abs footer__row" style="top:4078px">
    <span class="icon-circle"><svg width="14" height="18" viewBox="0 0 16 20"><path fill="#fff" d="M8 0a8 8 0 0 0-8 8c0 6 8 12 8 12s8-6 8-12a8 8 0 0 0-8-8zm0 11a3 3 0 1 1 0-6 3 3 0 0 1 0 6z"/></svg></span>
    <span>4120 Alder Row NE<br>Millbrook, MN 55990</span>
  </div>
  <div class="abs footer__row" style="top:4137px">
    <span class="icon-circle"><svg width="16" height="16" viewBox="0 0 24 24"><path fill="#fff" d="M6.6 10.8a15 15 0 0 0 6.6 6.6l2.2-2.2c.3-.3.7-.4 1-.2 1.1.4 2.3.6 3.6.6.6 0 1 .4 1 1V20c0 .6-.4 1-1 1A17 17 0 0 1 3 4c0-.6.4-1 1-1h3.5c.6 0 1 .4 1 1 0 1.3.2 2.5.6 3.6.1.3 0 .7-.2 1z"/></svg></span>
    <span>555 014 2290</span>
  </div>

  <h3 class="abs heading footer__head" style="left:745px">Links</h3>
  <a class="abs footer__link" href="#" style="left:745px;top:4075px">Home</a>
  <a class="abs footer__link" href="#" style="left:745px;top:4100px">Company</a>
  <a class="abs footer__link" href="#" style="left:745px;top:4125px">Service Area</a>
  <a class="abs footer__link" href="#" style="left:745px;top:4150px">Services</a>
  <a class="abs footer__link" href="#" style="left:884px;top:4075px">Gallery</a>
  <a class="abs footer__link" href="#" style="left:884px;top:4100px">Contact</a>
  <a class="abs footer__link" href="#" style="left:884px;top:4125px">FAQ</a>

  <span class="abs social" style="top:4029px" role="img" aria-label="Social profile link"></span>
  <span class="abs social" style="top:4080px" role="img" aria-label="Social profile link"></span>
  <span class="abs social" style="top:4130px" role="img" aria-label="Social profile link"></span>

  <p class="abs copyright">COPY RIGHTS © 2022 BRAMBLECOURT ELECTRIC<span>PRIVACY POLICY</span>TERMS &amp; CONDITIONS</p>

</div>
</body>
</html>
```